ソラベルデ調の24時間ジムです。
グランドオープン4月1日に向けてのチラシ作成依頼です。
24時間ジム月会費:6,500円(税抜)、パーソナルトレーニング月4回30分:16,000円(税抜)、パーソナルストレッチ月4回30分:16,000円(税抜)という3点を記載の上、パーソナルサービスご契約者様はご契約期間中は24時間ジム月会費無料というポイントを強調して下さい。
※パーソナルトレーニングとは、スタッフがお客様の目的を基にトレーニングメニュー作成とトレーニング補助を行います。また、食事等のご相談にもお答えします。
※パーソナルストレッチとは、スタッフがお客様の目的を基に、ストレッチによってお客様の凝りや不調を解消するサービスであり、トレーニング時の可動域増加、トレーニング後のリラックスとして利用頂けます。
ストレッチエリア、フリーウェイト、トレーニングマシン、有酸素マシンを完備している点を記載しても構いません。
空気清浄機を設置して換気は十分に行い、手指消毒、マシン消毒も徹底して行います。
店舗が茅ヶ崎市内にある為、「ミルコ」「海」「湘南」といった言葉を連想しつつも、一般大衆的なチラシの作成をお願いします。
配布も茅ヶ崎市内限定に限らせて頂くので、その点を強調しても構いません。
電話番号:0467-39-2751/住所:253-0086 神奈川県茅ヶ崎市浜見平3丁目2-9ミント・ハイツ中央2F・3F/ロゴ※添付資料としてお送りします。
A4
両面
茶系
• 高解像度JPG (.jpg)
• イラストレーター形式 (.ai)
• フォトショップ形式 (.psd)
• PNG形式 (.png)
以前、プレオープン用に作成したチラシに加えて、弊ジムロゴを添付致します。
どちらもai形式でお渡し可能です。
一点、修正点がございます。

月4回30分のパーソナルサービスを、月2回50分のパーソナルサービスに変更お願い致します。

価格設定は変更ございませんので、よろしくお願い致します。
ロゴ、チラシのaiファイルを添付しますので、ご活用よろしくお願い致します。

https://files.example-drop.test/a1b2c3d4e5

以上のリンク先より、ダウンロードの程、よろしくお願い致します。
申し訳ございません。

先程、追記致しましたパーソナルサービス内容は一旦破棄とさせて頂き、改めてお送り致します。

パーソナルトレーニング、パーソナルストレッチ共に月2回30分15,000円(税抜)、月4回30分22,000円(税抜)の内容となります。

上記内容で修正お願い致します。
https://files.example-drop.test/f6g7h8i9j0

店舗内装、外観を上記リンクにまとめました。

ご活用下さいませ。

内装のウッド調と海っぽさが調和した内容で、24時間ジムであることを謳いつつ、パーソナルサービスも提供していることも強調出来ていたので、選びました。

皆さま、短い期間で質の高いデザインを作成頂き、ありがとうございました。
今後も、チラシを作成する機会にございましたら、何卒宜しくお願い致します。

```html
<!DOCTYPE html>
<html lang="ja">
<head>
<meta charset="utf-8">
<title>ジムハーバー 茅ヶ崎24 グランドオープン</title>
<link rel="stylesheet" href="https://fonts.googleapis.com/css2?family=Playfair+Display:wght@700;900&family=Noto+Sans+JP:wght@400;700;900&family=M+PLUS+Rounded+1c:wght@800&display=swap">
<style>
:root{
  --wood:#8a5634;
  --wood-dark:#4e2e1b;
  --ink:#3a2418;
  --brown:#6b4326;
  --cream:#f7f2ea;
  --white:#ffffff;
  --accent:#e2532d;
  --photo-warm:#b98a66;
}
*{margin:0;padding:0;box-sizing:border-box}
html,body{width:849px;height:1200px;overflow:hidden;background:var(--cream)}
body{font-family:"Noto Sans JP",sans-serif;color:var(--ink)}
.flyer{position:relative;width:849px;height:1200px;overflow:hidden;background:var(--cream)}
.hero{position:absolute;left:0;top:0;width:849px;height:680px;
  background:linear-gradient(180deg,#a06a43 0%,var(--wood) 45%,#6f4127 100%)}
.hero-photo{position:absolute;left:470px;top:160px;width:280px;height:520px;
  background:linear-gradient(180deg,rgba(60,40,30,.15),rgba(40,30,25,.45))}
.brand{position:absolute;left:100px;top:40px;color:var(--white);
  font-family:"M PLUS Rounded 1c",sans-serif;font-weight:800}
.brand-name{font-size:58px;letter-spacing:2px;line-height:1}
.brand-sub{font-size:30px;text-align:center;margin-top:12px;letter-spacing:2px}
.tagline{position:absolute;left:752px;top:0;width:82px;height:320px;background:var(--white);
  writing-mode:vertical-rl;font-weight:900;font-size:24px;line-height:1.35;color:var(--brown);
  display:flex;align-items:center;justify-content:flex-start;padding-top:14px;letter-spacing:0;white-space:nowrap}
.headline{position:absolute;left:80px;top:165px;font-family:"Playfair Display",serif;
  font-weight:900;color:var(--ink);line-height:.95}
.headline span{display:block;font-size:150px}
.headline .open{padding-left:40px}
.date{position:absolute;left:350px;top:500px;font-family:"Playfair Display",serif;
  font-weight:900;font-size:56px;color:var(--white);letter-spacing:2px}
.intro{position:absolute;left:95px;top:592px;color:var(--white);font-size:19px;
  font-weight:700;line-height:1.65}
.entry-badge{position:absolute;left:38px;top:705px;width:135px;height:95px;
  background:var(--accent);color:var(--white);border-radius:14px;transform:rotate(-6deg);
  display:flex;flex-direction:column;align-items:center;justify-content:center;font-weight:900}
.entry-badge .label{font-size:22px}
.entry-badge .value{font-size:36px;line-height:1}
.fee{position:absolute;left:60px;top:812px;white-space:nowrap}
.fee-label{display:inline-block;background:var(--brown);color:var(--white);font-weight:700;
  font-size:22px;padding:4px 26px;border-radius:4px;margin-left:40px}
.fee-price{font-weight:900;color:var(--brown);font-size:80px;line-height:1.05;letter-spacing:1px}
.fee-price small{font-size:34px}
.fee-price em{font-style:normal;font-size:20px}
.free-box{position:absolute;left:535px;top:690px;width:290px;height:145px;
  background:var(--white);border:4px solid var(--brown);text-align:center;padding-top:12px}
.free-box .lead{font-size:18px;font-weight:700;color:var(--brown)}
.free-box .big{font-size:42px;font-weight:900;color:var(--ink);line-height:1.1}
.free-box .big b{color:var(--accent)}
.photo-strip{position:absolute;left:440px;top:850px;width:390px;height:100px;display:flex;gap:8px}
.photo-strip div{flex:1;background:linear-gradient(160deg,var(--photo-warm),#6f5546)}
.footer-brand{position:absolute;left:50px;top:960px;color:var(--brown);
  font-family:"M PLUS Rounded 1c",sans-serif;font-weight:800}
.footer-brand .name{font-size:44px;line-height:1}
.footer-brand .sub{font-size:22px;margin-top:6px;padding-left:80px}
.visit{position:absolute;left:50px;top:1045px;font-size:17px;font-weight:700;color:var(--ink)}
.phone{position:absolute;left:50px;top:1070px;display:flex;align-items:center;gap:10px;
  font-size:40px;font-weight:900;color:var(--ink);line-height:1.2}
.hours{position:absolute;left:50px;top:1124px;font-size:12px;color:var(--ink)}
.address{position:absolute;left:50px;top:1143px;font-size:12px;line-height:1.5;color:var(--ink)}
.map{position:absolute;left:440px;top:965px;width:390px;height:215px;
  background:linear-gradient(180deg,#ffffff,#ece6dc);border:2px solid var(--brown)}
</style>
</head>
<body>
<main class="flyer">
  <section class="hero">
    <div class="hero-photo" role="img" aria-label="トレッドミルの横に立つトレーニングウェアの女性の写真"></div>
    <div class="brand">
      <div class="brand-name">ジムハーバー</div>
      <div class="brand-sub">茅ヶ崎24</div>
    </div>
    <div class="tagline">好きな時間に好きな<br>だけトレーニング&amp;有酸素</div>
    <h1 class="headline"><span>Grand</span><span class="open">Open</span></h1>
    <p class="date">2021.4.1</p>
    <p class="intro">ストレッチエリア、フリーウェイト、トレーニングマシン、有酸素マシン完備<br>ジムハーバー茅ヶ崎24でトレーニングを始めてみませんか？</p>
  </section>

  <div class="entry-badge"><span class="label">入会金</span><span class="value">0円!</span></div>

  <div class="fee">
    <div class="fee-label">24時間ジム月会費</div>
    <div class="fee-price">6,500<small>円</small><em>(税抜)</em></div>
  </div>

  <div class="free-box">
    <p class="lead">パーソナルサービス利用で</p>
    <p class="big">24時間ジム<br>月会費<b>無料</b></p>
  </div>

  <div class="photo-strip">
    <div role="img" aria-label="パーソナルトレーニングの様子の写真"></div>
    <div role="img" aria-label="パーソナルストレッチの様子の写真"></div>
  </div>

  <div class="footer-brand">
    <div class="name">ジムハーバー</div>
    <div class="sub">茅ヶ崎24</div>
  </div>
  <p class="visit">駅歩き7分！無料見学随時大歓迎！</p>
  <p class="phone">
    <svg width="38" height="38" viewBox="0 0 24 24" aria-hidden="true"><circle cx="12" cy="12" r="11" fill="none" stroke="#3a2418" stroke-width="2"/><path d="M8 6.5l2 0 1 3-1.3 1a7 7 0 0 0 3.8 3.8l1-1.3 3 1v2a1.5 1.5 0 0 1-1.6 1.5A10 10 0 0 1 6.5 8.1 1.5 1.5 0 0 1 8 6.5z" fill="#3a2418"/></svg>
    0467-39-2751
  </p>
  <p class="hours">【電話受付時間 10:00～22:00】</p>
  <p class="address">253-0086 神奈川県茅ヶ崎市浜見平3丁目2-9<br>ミント・ハイツ中央2F・3F</p>

  <div class="map" role="img" aria-label="茅ヶ崎駅から店舗までの道順を示す地図"></div>
</main>
</body>
</html>
```